Food Platform with Economic-Social Cause, needs folder design, corporate and stationery

Technology company linked to food with strong social commitment, needs to dazzle customers and shareholders, with elegant, minimalist and distinguished design of folder, corporate card and other stationery. The Company proposes networking by creating a community committed to the economic and social aspects. The humanization of the economy. We attach a model of another company card and logo to use in proposals.
UNFORTUNATELY WE CANNOT FIND A DESIGN THAT DOES NOT REPRESENT WHAT WE ARE LOOKING FOR
Target Market(s)
Companies, entrepreneurs, food producers and the general public
Industry/Entity Type
Food companies, Foundations fight against hunger, Citizenship.
Colors
Designer to choose colors to be used in the design.
Requirements
Must have
- elegance, minimalism, graphic communication of networking for a humanized economy. phrase "activating consciousness" "united for a cause"
Nice to have
- human network graph. Chain of favors. Preferred shades: white, gold or champagne and combination.human network graph. Chain of favors. Preferred shades: white, gold or champagne and combination.
Should not have
- dark communication

```html
<!DOCTYPE html>
<html lang="en">
<head>
<meta charset="utf-8">
<title>Unitia – Presentation Folder</title>
<link href="https://fonts.googleapis.com/css2?family=Archivo+Black&family=Rubik:wght@400;500;700&display=swap" rel="stylesheet">
<style>
  :root{
    --stage:#e4e4e4;
    --paper:#f7f7f7;
    --paper-shade:#ececec;
    --gold-dark:#6f5622;
    --gold:#a5822f;
    --gold-light:#b8933d;
    --ink:#141414;
    --charcoal:#2a2a2a;
    --watermark:#d2d2d2;
    --map-tone:#ddd6c8;
    --white:#ffffff;
  }
  *{box-sizing:border-box;margin:0;padding:0}
  html,body{width:850px;height:1200px;overflow:hidden}
  body{background:var(--stage);font-family:"Rubik",sans-serif;position:relative}

  .spread{position:absolute;left:45px;width:760px;height:500px;display:flex;box-shadow:0 14px 30px rgba(0,0,0,.18)}
  .spread--outer{top:45px}
  .spread--inner{top:640px}
  .panel{position:relative;width:380px;height:500px;overflow:hidden}

  /* back cover */
  .back-cover{background:linear-gradient(120deg,var(--gold-dark) 0%,var(--gold-light) 35%,var(--gold) 60%,var(--gold-dark) 100%);color:var(--white)}
  .back-cover .brand-name{position:absolute;left:0;right:0;top:170px;text-align:center;font-weight:500;font-size:64px;letter-spacing:1px;color:var(--white)}
  .follow{position:absolute;right:32px;bottom:120px;text-align:right}
  .follow__label{font-weight:700;font-size:11px;letter-spacing:.5px;border-bottom:1px solid var(--white);padding-bottom:2px;display:inline-block}
  .follow__icons{display:flex;gap:6px;justify-content:flex-end;margin-top:8px}
  .follow__icons span{width:18px;height:18px;border-radius:50%;background:var(--white);display:block}
  .back-cover .web{position:absolute;right:32px;bottom:90px;font-size:12px;letter-spacing:.8px}
  .office{position:absolute;left:32px;bottom:40px;font-size:10.5px;line-height:1.35;font-style:normal;font-weight:400}
  .office strong{font-weight:700;font-size:11px}

  /* front cover */
  .front-cover{background:linear-gradient(180deg,var(--white),var(--paper))}
  .front-cover .brand-name{position:absolute;left:0;right:0;top:58px;text-align:center;font-weight:500;font-size:44px;color:var(--gold)}
  .front-cover .brand-dot{display:inline-block;width:12px;height:12px;border-radius:50%;background:var(--gold);margin-left:6px;vertical-align:middle}
  .network-visual{position:absolute;left:0;top:150px;width:380px;height:200px;background:radial-gradient(ellipse at 55% 45%,var(--map-tone) 0%,#ebe8e2 55%,#f0f0f0 100%)}
  .headline{position:absolute;left:0;right:0;top:366px;text-align:center;font-family:"Archivo Black",sans-serif;font-weight:400;font-synthesis:none;line-height:1.08;letter-spacing:.5px}
  .headline__top{display:block;font-size:28px;color:var(--ink)}
  .headline__bottom{display:block;font-size:31px;color:var(--gold)}
  .front-cover .web{position:absolute;left:0;right:0;bottom:42px;text-align:center;font-size:12px;letter-spacing:.8px;color:var(--charcoal)}

  /* inner spread */
  .inner{background:linear-gradient(180deg,var(--paper),var(--paper-shade))}
  .inner + .inner{border-left:1px solid #d6d6d6}
  .watermark{position:absolute;left:0;right:0;top:110px;text-align:center;font-weight:500;font-size:60px;color:var(--watermark)}
  .pocket{position:absolute;left:0;right:0;bottom:0;height:175px;border-radius:16px 16px 0 0}
  .pocket--black{background:var(--charcoal);height:160px;z-index:2}
  .pocket--gold{background:linear-gradient(100deg,var(--gold-dark),var(--gold-light) 60%,var(--gold))}
  .disc{position:absolute;left:90px;bottom:120px;width:180px;height:180px;border-radius:50%;background:radial-gradient(circle,#bbb 0 16px,#333 17px 100%)}

  .card{position:absolute;left:85px;bottom:62px;width:210px;height:100px;background:var(--ink);color:var(--white);display:flex;align-items:center;gap:12px;padding:0 14px}
  .card__name{font-weight:500;font-size:17px;color:var(--gold-light)}
  .card__contact{font-size:7.5px;line-height:1.45}
</style>
</head>
<body>

  <section class="spread spread--outer">
    <article class="panel back-cover">
      <div class="brand-name">Unitia</div>
      <div class="follow">
        <span class="follow__label">FOLLOW US ON</span>
        <div class="follow__icons"><span></span><span></span><span></span></div>
      </div>
      <div class="web">www.unitia-network.org</div>
      <address class="office">
        <strong>Head Office</strong><br>
        1234, Lorem Ipsum Tower 1<br>
        PO. Box 1234500<br>
        Lorem, Dolor sit<br>
        Tel: +123 45 3351360
      </address>
    </article>

    <article class="panel front-cover">
      <div class="brand-name">Unitia<span class="brand-dot"></span></div>
      <div class="network-visual" role="img" aria-label="World map with a connected network of people across continents"></div>
      <h1 class="headline">
        <span class="headline__top">ACTIVATING</span>
        <span class="headline__bottom">CONSCIOUSNESS</span>
      </h1>
      <div class="web">www.unitia-network.org</div>
    </article>
  </section>

  <section class="spread spread--inner">
    <article class="panel inner">
      <div class="watermark">Unitia</div>
      <div class="disc" role="img" aria-label="Branded disc tucked into the pocket"></div>
      <div class="pocket pocket--black"></div>
    </article>

    <article class="panel inner">
      <div class="watermark">Unitia</div>
      <div class="pocket pocket--gold">
        <div class="card">
          <span class="card__name">Unitia</span>
          <p class="card__contact">
            18 Meridian Way, Suite 4<br>
            Harlow Bay, CA 90210<br>
            Tel: 555 014-2290<br>
            www.unitia-network.org
          </p>
        </div>
      </div>
    </article>
  </section>

</body>
</html>
```